International MultiIndustry Team Coaching Site

Hello Designers,
We need a redesign of the pages attached.
The design must be engaging and modern, with a focus on the user experience, particularly for the "observations" page. Because this is the main page of the website. It is to be used on a 10'' tablet or desktop, to record observations on the fly, so it must be intuitive and efficient.
The positioning of the metrics and observations and etc, are just a reference. you can switch it up if you feel there is a better way (PLEASE DO ;) ).

There are many categories (color coded with borders in the example hpt_6_observations.jpg) and observation metrics within each category. This is the Key page, because it is the One with the most interactions.

The user should know when it has selected a category (there should be some visual hint) and the different metric widgets should be accounted for.
There are 3: The time widget at the end, numerical widgets (recording more or less numbers), and boolean ones (selected or not).

For the numerical widgets, we show plus and minus characters, but you can change this, being creative, keeping in mind that it must work well on a mobile device and desktop, and must be intuitive and quick.

Set your creativity free with the login screen , home screen, categories secret, events screen, journaling and observations screen .

We would like the site/mobile version to have a very modern look. Something that would be found in very popular and user friendly apps.

***** The events, journaling, category and home screens are getting 2 much attention , please focus also on the observations screen *******
Imagine you are a psychologist tasked with observing the behaviour of teenagers during group work. And you have a tablet on which to record what you observe. Now imagine you need to observe during 3 classes: Biology, Math, Physics (these are events). For each class (event) you will have to record observations in 3 categories: Social Interaction, Leadership, Communication (these are categories).
Example of the metrics (these are observations) for Leadership:
" the teenager direct other colleagues" (boolean widget),
"the teenager speaks more than everyone else" (boolean widget)
"the teenager interrupts colleagues speaking" (number widget)
"the work took hh:mm" (time widget)

The observations screen can have any shape and form you think of. It doesn't need to be that single column with yes and nos, or that double column with the squared cards.
thank you.

Hope that was useful intel :)
Available for any questions you might have.
Good luck :)

Target Market(s)

Enterprise teams

Number of Pages Required

5+ page

Font styles to use
Sans Serif

Requirements
Must have
• Modern design

```html
<!DOCTYPE html>
<html lang="en">
<head>
<meta charset="UTF-8">
<title>Huddle – Grass Team-3 Events</title>
<link rel="stylesheet" href="https://fonts.googleapis.com/css2?family=Poppins:wght@400;500;600;700&display=swap">
<style>
  :root {
    --page-bg: #f4f6fa;
    --page-tint: #e6ecf6;
    --header-bg: #ffffff;
    --line: #e3e6ee;
    --ink: #252a40;
    --ink-soft: #3c4052;
    --muted: #6b6f82;
    --accent-blue: #4c82c3;
    --accent-purple: #4d3f8f;
    --accent-purple-line: #5d519e;
    --page-active: #5d6294;
    --page-line: #9ea3b5;
    --card-bg: #ffffff;
    --toggle-bg: #4c82c3;
    --photo-warm-a: #d9d2c4;
    --photo-warm-b: #8c7a63;
    --photo-cool-a: #eef0f2;
    --photo-cool-b: #c7cdd6;
    --avatar-a: #d7dbe6;
    --avatar-b: #4b5064;
  }
  * { box-sizing: border-box; margin: 0; padding: 0; }
  html, body { width: 1200px; height: 696px; overflow: hidden; }
  body {
    font-family: "Poppins", sans-serif;
    color: var(--ink);
    background:
      radial-gradient(ellipse 700px 260px at 620px 400px, var(--page-tint), transparent 70%),
      var(--page-bg);
    position: relative;
  }

  /* Header */
  .site-header {
    height: 67px;
    background: var(--header-bg);
    border-bottom: 1px solid var(--line);
    display: flex;
    align-items: center;
    padding: 0 25px;
  }
  .brand {
    display: flex; align-items: center; gap: 8px;
    font-size: 23px; font-weight: 700; color: var(--ink);
  }
  .brand-dot { width: 20px; height: 20px; border-radius: 50%; background: var(--accent-purple); }
  .header-tools { margin-left: auto; display: flex; align-items: center; }
  .theme-toggle {
    width: 38px; height: 18px; border-radius: 9px; background: var(--toggle-bg);
    position: relative; margin-right: 24px;
  }
  .theme-toggle svg { position: absolute; left: 5px; top: 3px; }
  .theme-toggle::after {
    content: ""; position: absolute; right: 3px; top: 3px;
    width: 12px; height: 12px; border-radius: 50%; background: #fff;
  }
  .avatar {
    width: 34px; height: 34px; border-radius: 50%;
    background: linear-gradient(160deg, var(--avatar-a) 40%, var(--avatar-b));
    border: 1px solid var(--line);
    margin-right: 10px;
  }
  .owner-name { font-size: 12px; color: var(--muted); margin-right: 12px; }

  /* Page head */
  .page-head {
    display: flex; align-items: center; justify-content: space-between;
    padding: 39px 25px 0 25px; height: 106px;
  }
  .page-title { font-size: 20px; font-weight: 600; color: var(--ink); }
  .back-button {
    width: 83px; height: 38px; border: 1px solid var(--accent-blue); border-radius: 4px;
    background: #fff; color: var(--accent-blue); font-family: inherit;
    font-size: 13px; font-weight: 500; display: flex; align-items: center; justify-content: center; gap: 10px;
  }

  /* Events grid */
  .event-grid {
    display: grid;
    grid-template-columns: 562px 563px;
    column-gap: 26px; row-gap: 25px;
    padding: 22px 25px 0 25px;
  }
  .event-card {
    height: 208px; background: var(--card-bg); border-radius: 6px;
    box-shadow: 0 2px 10px rgba(40, 50, 90, 0.05);
    display: flex; padding: 8px; position: relative;
  }
  .event-photo { width: 179px; height: 192px; border-radius: 6px; flex-shrink: 0; }
  .event-photo.lounge { background: linear-gradient(150deg, var(--photo-warm-a) 10%, #b8a68a 55%, var(--photo-warm-b)); }
  .event-photo.whiteboard { background: linear-gradient(180deg, var(--photo-cool-a) 55%, var(--photo-cool-b)); }
  .event-body { padding: 9px 0 0 21px; flex: 1; }
  .event-title { font-size: 17px; font-weight: 500; color: var(--accent-blue); line-height: 22px; }
  .event-date {
    display: flex; align-items: center; gap: 8px;
    font-size: 11px; font-weight: 500; color: var(--ink-soft); margin-top: 8px;
  }
  .event-summary {
    font-size: 11.2px; line-height: 18.3px; color: var(--ink-soft);
    margin-top: 16px; max-width: 330px;
  }
  .add-observation {
    position: absolute; right: 16px; bottom: 17px;
    width: 160px; height: 38px; background: #fff;
    border: 1px solid var(--accent-purple-line); border-radius: 4px;
    color: var(--accent-purple); font-family: inherit; font-size: 12.5px; font-weight: 500;
    display: flex; align-items: center; justify-content: center; gap: 9px;
  }

  /* Pagination */
  .pagination {
    position: absolute; top: 643px; left: 565px;
    display: flex; gap: 5px;
  }
  .page-link {
    width: 20px; height: 20px; border: 1px solid var(--page-line); border-radius: 3px;
    font-size: 11px; color: var(--muted); display: flex; align-items: center; justify-content: center;
    background: #fff;
  }
  .page-link.is-active { background: var(--page-active); border-color: var(--page-active); color: #fff; font-weight: 600; }
  .page-link.is-disabled { border-color: var(--line); opacity: 0.6; }
</style>
</head>
<body>
  <header class="site-header">
    <div class="brand"><span class="brand-dot"></span>Huddle</div>
    <div class="header-tools">
      <div class="theme-toggle" aria-label="Theme toggle">
        <svg width="11" height="11" viewBox="0 0 12 12" fill="none" stroke="#fff" stroke-width="1.1">
          <circle cx="6" cy="6" r="2.3"/>
          <path d="M6 0.5v1.6M6 9.9v1.6M0.5 6h1.6M9.9 6h1.6M2.1 2.1l1.1 1.1M8.8 8.8l1.1 1.1M2.1 9.9l1.1-1.1M8.8 3.2l1.1-1.1"/>
        </svg>
      </div>
      <div class="avatar" role="img" aria-label="Profile photo of the account owner"></div>
      <span class="owner-name">Owner name</span>
      <svg width="14" height="8" viewBox="0 0 14 8" fill="none" stroke="#3c4052" stroke-width="1.5"><path d="M1 1l6 6 6-6"/></svg>
    </div>
  </header>

  <section class="page-head">
    <h1 class="page-title">Grass Team-3</h1>
    <button class="back-button">
      <svg width="9" height="16" viewBox="0 0 9 16" fill="none" stroke="currentColor" stroke-width="1.5"><path d="M8 1L1 8l7 7"/></svg>
      Back
    </button>
  </section>

  <main class="event-grid">
    <article class="event-card">
      <div class="event-photo lounge" role="img" aria-label="Team members talking in a lounge with sticky notes on the wall"></div>
      <div class="event-body">
        <h2 class="event-title">Event 1</h2>
        <p class="event-date">
          <svg width="15" height="15" viewBox="0 0 16 16" fill="none" stroke="#6b6f82" stroke-width="1.2"><rect x="1.5" y="2.5" width="13" height="12" rx="1.5"/><path d="M1.5 6h13M5 1v3M11 1v3"/></svg>
          08/10/2022 , 09:45AM
        </p>
        <p class="event-summary">Lorem Ipsum is simply dummy text of the printing and typesetting industry. Lorem Ipsum has been the industry's standard dummy text ever since the..</p>
      </div>
      <button class="add-observation">
        <svg width="18" height="18" viewBox="0 0 18 18" fill="none" stroke="currentColor" stroke-width="1.4"><path d="M9 1v16M1 9h16"/></svg>
        Add Observation
      </button>
    </article>

    <article class="event-card">
      <div class="event-photo whiteboard" role="img" aria-label="Two colleagues working at a whiteboard above a table with a laptop"></div>
      <div class="event-body">
        <h2 class="event-title">Event 2</h2>
        <p class="event-date">
          <svg width="15" height="15" viewBox="0 0 16 16" fill="none" stroke="#6b6f82" stroke-width="1.2"><rect x="1.5" y="2.5" width="13" height="12" rx="1.5"/><path d="M1.5 6h13M5 1v3M11 1v3"/></svg>
          08/10/2022 , 09:45AM
        </p>
        <p class="event-summary">Lorem Ipsum is simply dummy text of the printing and typesetting industry. Lorem Ipsum has been the industry's standard dummy text ever since the..</p>
      </div>
      <button class="add-observation">
        <svg width="18" height="18" viewBox="0 0 18 18" fill="none" stroke="currentColor" stroke-width="1.4"><path d="M9 1v16M1 9h16"/></svg>
        Add Observation
      </button>
    </article>

    <article class="event-card">
      <div class="event-photo lounge" role="img" aria-label="Team members talking in a lounge with sticky notes on the wall"></div>
      <div class="event-body">
        <h2 class="event-title">Event 4</h2>
        <p class="event-date">
          <svg width="15" height="15" viewBox="0 0 16 16" fill="none" stroke="#6b6f82" stroke-width="1.2"><rect x="1.5" y="2.5" width="13" height="12" rx="1.5"/><path d="M1.5 6h13M5 1v3M11 1v3"/></svg>
          08/10/2022 , 09:45AM
        </p>
        <p class="event-summary">Lorem Ipsum is simply dummy text of the printing and typesetting industry. Lorem Ipsum has been the industry's standard dummy text ever since the..</p>
      </div>
      <button class="add-observation">
        <svg width="18" height="18" viewBox="0 0 18 18" fill="none" stroke="currentColor" stroke-width="1.4"><path d="M9 1v16M1 9h16"/></svg>
        Add Observation
      </button>
    </article>

    <article class="event-card">
      <div class="event-photo whiteboard" role="img" aria-label="Two colleagues working at a whiteboard above a table with a laptop"></div>
      <div class="event-body">
        <h2 class="event-title">Event 5</h2>
        <p class="event-date">
          <svg width="15" height="15" viewBox="0 0 16 16" fill="none" stroke="#6b6f82" stroke-width="1.2"><rect x="1.5" y="2.5" width="13" height="12" rx="1.5"/><path d="M1.5 6h13M5 1v3M11 1v3"/></svg>
          08/10/2022 , 09:45AM
        </p>
        <p class="event-summary">Lorem Ipsum is simply dummy text of the printing and typesetting industry. Lorem Ipsum has been the industry's standard dummy text ever since the..</p>
      </div>
      <button class="add-observation">
        <svg width="18" height="18" viewBox="0 0 18 18" fill="none" stroke="currentColor" stroke-width="1.4"><path d="M9 1v16M1 9h16"/></svg>
        Add Observation
      </button>
    </article>
  </main>

  <nav class="pagination" aria-label="Pagination">
    <span class="page-link is-disabled"><svg width="6" height="10" viewBox="0 0 6 10" fill="none" stroke="#9ea3b5" stroke-width="1.2"><path d="M5 1L1 5l4 4"/></svg></span>
    <span class="page-link is-active">1</span>
    <span class="page-link">2</span>
    <span class="page-link">3</span>
    <span class="page-link"><svg width="6" height="10" viewBox="0 0 6 10" fill="none" stroke="#3c4052" stroke-width="1.2"><path d="M1 1l4 4-4 4"/></svg></span>
  </nav>
</body>
</html>
```